'Bright Ledger Hidden Keys' Book Cover

I need a professional book cover design for my new upcoming book that shows people how to get a high credit score.

Here are my two websites:

https://www.moneywordbank-lexa.info
https://moneywordbank-lexa.com/

I am looking for a clean, professional design that pops (emotional touch) and separates from the other books that are on the market. Cover aspect ratio 1:4 for Pagewisp version and 1:5 for the paperback version. Yellow or blue are good colors - but not must. See the basic examples that I provided. File delivery format PDF.

Book Title: Bright Ledger Hidden Keys
Byline: The Quick Lift And Mend Manual for Stellar Borrowing

Currently on Brindlecart pre-order:
https://www.brindlecart.example/Bright-Ledger-Hidden-Keys-Stellar-ebook/dp/Q48MPLRT71

I am the author of 36 published books on Brindlecart. My author profile is here:
brindlecart.example/author/gideonvarly

Targeted audience: People that want to improve or repair their bad credit score.

Target Market(s)

People/consumers in the US that want to improve or repair their credit score.

Industry/Entity Type

Consumer

Font styles to use
Sans Serif

Colors

Designer to choose colors to be used in the design.

Requirements
Must have
• Author name, Title, byline, and graphic element(s).
Nice to have
• - 2020 edition logo / batch

```html
<!DOCTYPE html>
<html lang="en">
<head>
<meta charset="utf-8">
<title>Bright Ledger Hidden Keys — Book Cover</title>
<link rel="stylesheet" href="https://fonts.googleapis.com/css2?family=Bebas+Neue&family=Questrial&display=swap">
<style>
  :root {
    --paper: #ffffff;
    --title-blue: #0399cc;
    --title-red: #cf1229;
    --band-maroon: #7a0f1f;
    --band-text: #ffffff;
    --author-plum: #4a2030;
    --card-deep: #5a1826;
    --card-mid: #8c1a2c;
    --card-bright: #c8162a;
  }
  html, body {
    margin: 0;
    padding: 0;
    width: 800px;
    height: 1200px;
    overflow: hidden;
    background: var(--paper);
  }
  .cover {
    position: relative;
    width: 800px;
    height: 1200px;
    background: var(--paper);
  }
  .cover-art {
    position: absolute;
    left: 0;
    top: 0;
    width: 800px;
    height: 1200px;
  }
  .title-line,
  .author-name {
    font-family: 'Bebas Neue', 'Oswald', sans-serif;
  }
  .title-blue { fill: var(--title-blue); }
  .title-red { fill: var(--title-red); }
  .author-name { fill: var(--author-plum); }
  .subtitle-band {
    position: absolute;
    left: 122px;
    top: 570px;
    width: 561px;
    height: 102px;
    background: var(--band-maroon);
    display: flex;
    align-items: center;
    justify-content: center;
  }
  .subtitle {
    margin: 0;
    font-family: 'Questrial', 'Century Gothic', sans-serif;
    font-weight: 400;
    color: var(--band-text);
    font-size: 33px;
    line-height: 42px;
    text-align: center;
  }
</style>
</head>
<body>
  <main class="cover">
    <svg class="cover-art" viewBox="0 0 800 1200" xmlns="http://www.w3.org/2000/svg">
      <defs>
        <linearGradient id="card-fill" x1="0" y1="0" x2="1" y2="1">
          <stop offset="0" stop-color="#6e2a36"/>
          <stop offset="0.5" stop-color="#c8162a"/>
          <stop offset="1" stop-color="#5a1826"/>
        </linearGradient>
        <radialGradient id="card-shadow" cx="0.5" cy="0.5" r="0.5">
          <stop offset="0" stop-color="#000" stop-opacity="0.12"/>
          <stop offset="1" stop-color="#000" stop-opacity="0"/>
        </radialGradient>
      </defs>

      <text class="title-line title-blue" x="117" y="163" font-size="157" textLength="566" lengthAdjust="spacingAndGlyphs">BRIGHT LEDGER</text>
      <text class="title-line title-blue" x="117" y="360" font-size="257" textLength="566" lengthAdjust="spacingAndGlyphs">HIDDEN</text>
      <text class="title-line title-red" x="117" y="533" font-size="226" textLength="566" lengthAdjust="spacingAndGlyphs">KEYS</text>

      <g class="card-illustration" role="img" aria-label="Illustration of a tilted dark red credit card with a gold chip">
        <ellipse cx="400" cy="1045" rx="230" ry="22" fill="url(#card-shadow)"/>
        <polygon points="227,694 645,809 582,1054 166,936" fill="url(#card-fill)" stroke="#5a1826" stroke-width="6" stroke-linejoin="round"/>
      </g>

      <text class="author-name" x="207" y="1156" font-size="90" textLength="422" lengthAdjust="spacingAndGlyphs">GIDEON VARLY</text>
    </svg>

    <div class="subtitle-band">
      <p class="subtitle">The Quick Lift And Mend Manual<br>for Stellar Borrowing</p>
    </div>
  </main>
</body>
</html>
```